Business Card Design - BVN (company name)

Over 20 years of progressive technology design, migration and management experience that drives business objectives and streamlines operations. Continuously challenge conventions to meet and exceed business security, availability and functionality requirements. Maintain exceptional vendor relationships to ensure ongoing knowledge of emerging products and to secure preferred service agreements. Recruit and utilize top talent and foster a collegial environment that advances innovation and performance excellence. design logo using 3 arrows of different colors green, gold, blue

Industry/Entity Type

Progressive

Contact Information for Business Card

Martin K. Osei
IT Strategist / Consultant

555.302.8846 MOsei@bvnorel.example 3817 Wrenfield Court Pasadena, CA 91877

Colors
0255a3
f37122
fece3e

Requirements
Must have
• Note NEW EMAIL ADDRESS
• MOsei@bvnorel.example
• NOTE NEW ORDER of the work I do.
• Infrastructure – Systems – Cybersecurity
Nice to have
• main color should be orange

```html
<!DOCTYPE html>
<html lang="en">
<head>
<meta charset="utf-8">
<title>BVN – Business Card</title>
<link rel="stylesheet" href="https://fonts.googleapis.com/css2?family=Lato:ital,wght@0,400;0,700;0,900;1,400&display=swap">
<style>
  :root {
    --page-bg: #e4e4e4;
    --card-white: #ffffff;
    --card-black: #050505;
    --ink: #1c1c1c;
    --ink-soft: #3a3a3a;
    --green: #1fa24f;
    --gold: #f6b81c;
    --blue: #4a9fd6;
    --dash-grey: #9a9a9a;
    --mark-grey: #dde1e6;
  }
  * { box-sizing: border-box; margin: 0; padding: 0; }
  html, body {
    width: 1200px; height: 926px; overflow: hidden;
    background: var(--page-bg);
    font-family: "Lato", Arial, sans-serif;
  }
  .canvas { position: relative; width: 1200px; height: 926px; }
  .card {
    position: absolute; left: 250px; width: 700px; height: 400px;
    overflow: hidden;
    box-shadow: 0 6px 18px rgba(0,0,0,.18);
  }
  .card--back { top: 42px; background: var(--card-black); }
  .card--front { top: 484px; background: var(--card-white); }

  /* service line */
  .tagline {
    font-weight: 700; font-size: 21px; letter-spacing: 4px;
    text-transform: uppercase; white-space: nowrap;
  }
  .tagline .t-infra { color: var(--gold); }
  .tagline .t-systems { color: var(--green); }
  .tagline .t-cyber { color: var(--blue); }
  .tagline .t-dash { color: var(--dash-grey); margin: 0 8px; }

  /* back */
  .back-brand {
    position: absolute; left: 0; right: 0; top: 110px;
    display: flex; align-items: center; justify-content: center; gap: 16px;
  }
  .back-brand .brand-dot {
    width: 40px; height: 40px; border-radius: 50%; background: var(--gold);
  }
  .back-brand .brand-name {
    font-weight: 900; font-size: 72px; color: #ffffff; letter-spacing: 4px;
  }
  .card--back .tagline {
    position: absolute; left: 0; right: 0; top: 262px; text-align: center;
  }

  /* front */
  .identity {
    position: absolute; left: 38px; top: 46px;
    display: flex; align-items: center; gap: 16px;
  }
  .identity .brand-mark { display: flex; align-items: center; gap: 8px; }
  .identity .brand-dot {
    width: 16px; height: 16px; border-radius: 50%; background: var(--gold);
  }
  .identity .brand-name {
    font-weight: 900; font-size: 24px; color: var(--blue); letter-spacing: 1px;
  }
  .person-name {
    font-size: 30px; color: var(--ink); letter-spacing: .5px; line-height: 1;
    text-transform: uppercase;
  }
  .person-name b { font-weight: 900; }
  .person-name span { font-weight: 400; }
  .person-title {
    font-style: italic; font-size: 19px; color: var(--ink-soft); margin-top: 4px;
  }

  .contact-list {
    position: absolute; left: 40px; top: 168px; list-style: none;
  }
  .contact-list li {
    display: flex; align-items: center; gap: 12px;
    font-size: 17px; color: var(--ink-soft); line-height: 26px;
  }
  .contact-list svg { width: 14px; height: 14px; fill: var(--ink); flex: none; }

  .brand-watermark {
    position: absolute; right: 30px; top: 128px;
    font-weight: 900; font-size: 120px; line-height: 1; color: var(--mark-grey);
    letter-spacing: 2px;
  }

  .front-band {
    position: absolute; left: 0; right: 0; bottom: 0; height: 84px;
    background: var(--card-black);
    display: flex; align-items: center; justify-content: center;
  }
</style>
</head>
<body>
<main class="canvas">

  <section class="card card--back" aria-label="Business card back">
    <div class="back-brand">
      <span class="brand-dot"></span>
      <span class="brand-name">BVN</span>
    </div>
    <p class="tagline">
      <span class="t-infra">Infrastructure</span><span class="t-dash">–</span><span class="t-systems">Systems</span><span class="t-dash">–</span><span class="t-cyber">Cybersecurity</span>
    </p>
  </section>

  <section class="card card--front" aria-label="Business card front">
    <div class="identity">
      <div class="brand-mark">
        <span class="brand-dot"></span>
        <span class="brand-name">BVN</span>
      </div>
      <div>
        <h1 class="person-name"><b>Martin</b> <span>K. Osei</span></h1>
        <p class="person-title">IT Strategist / Consultant</p>
      </div>
    </div>

    <ul class="contact-list">
      <li>
        <svg viewBox="0 0 16 16" aria-hidden="true"><path d="M3.6 1.2l2.3 2.6-1.3 2.1c.9 1.9 2.3 3.4 4.3 4.4l2.1-1.3 2.6 2.3-1.4 2.4C6.8 13.7 2.3 9.2 1.3 3.1z"/></svg>
        555.302.8846
      </li>
      <li>
        <svg viewBox="0 0 16 16" aria-hidden="true"><path d="M1 3h14v10H1zM2.4 4.2L8 8.6l5.6-4.4z" fill-rule="evenodd"/></svg>
        MOsei@bvnorel.example
      </li>
      <li>
        <svg viewBox="0 0 16 16" aria-hidden="true"><path d="M8 0.5a5 5 0 0 0-5 5c0 3.8 5 10 5 10s5-6.2 5-10a5 5 0 0 0-5-5zm0 7a2 2 0 1 1 0-4 2 2 0 0 1 0 4z"/></svg>
        3817 Wrenfield Court Pasadena, CA 91877
      </li>
    </ul>

    <span class="brand-watermark" aria-hidden="true">BVN</span>

    <div class="front-band">
      <p class="tagline">
        <span class="t-infra">Infrastructure</span><span class="t-dash">–</span><span class="t-systems">Systems</span><span class="t-dash">–</span><span class="t-cyber">Cybersecurity</span>
      </p>
    </div>
  </section>

</main>
</body>
</html>
```